Template für Webova-Page
Zielgruppe
Geschlecht: ca. 90% Männlich
Alter: ca. 30-60 Jahre
höheres Einkommen, höhere Bildung
Aufgabenstellung
FORNVALT ist ein Netzwerk von Maßschuhmachern. Die Schuhmacher werden auf der Webseite gefunden und es wird ein Eindruck der Möglichkeiten des Maßschuhmachens vermittelt.
Aufgrund der offenen Struktur arbeiten wir derzeit mit Webova, damit jeder Schuhmacher die Möglichkeit hat, Inhalte einzustellen, zu pflegen und zu aktualisieren.
Webova scheint für diese Zwecke gut geeignet, hat aber kein adäquates Standard-Layout.
ES GEHT NUR UM DAS WEBDESIGN, NICHT UM DIE IMPLEMENTIERUNG!

```html
<!DOCTYPE html>
<html lang="de">
<head>
<meta charset="utf-8">
<title>FORNVALT – Maßschuhe à la carte</title>
<link href="https://fonts.googleapis.com/css2?family=Arimo:wght@400;700&display=swap" rel="stylesheet">
<style>
  :root {
    --bg-dark: #141414;
    --bg-mid: #2a2a2a;
    --panel: rgba(20,20,20,0.55);
    --bar-top: #3a3a3a;
    --bar-bottom: #121212;
    --gold: #c9a54a;
    --gold-light: #e3c373;
    --text: #f1f1f1;
    --muted: #c4c4c4;
    --divider: #050505;
  }
  * { margin: 0; padding: 0; box-sizing: border-box; }
  html, body { width: 1200px; height: 884px; overflow: hidden; }
  body {
    position: relative;
    font-family: "Arimo", Arial, sans-serif;
    color: var(--text);
    background:
      radial-gradient(ellipse at 30% 40%, #333 0%, transparent 55%),
      radial-gradient(ellipse at 85% 70%, #2c2c2c 0%, transparent 50%),
      linear-gradient(180deg, #1e1e1e, var(--bg-dark));
  }
  .brand {
    position: absolute; left: 18px; top: 30px; width: 150px;
    display: flex; flex-direction: column; align-items: center; gap: 10px;
  }
  .brand-dot { width: 38px; height: 38px; border-radius: 50%; border: 2px solid var(--gold); }
  .brand-name { font-size: 21px; font-weight: 700; color: var(--gold); letter-spacing: 0.5px; }

  .nav {
    position: absolute; left: 183px; top: 17px; width: 933px; height: 51px;
    border-radius: 5px 5px 0 0;
    background: linear-gradient(180deg, var(--bar-top), var(--bar-bottom));
    display: flex; align-items: center; padding-left: 27px; gap: 0;
  }
  .nav a {
    color: var(--text); text-decoration: none; font-size: 15px;
    letter-spacing: 0.6px; margin-right: 38px;
  }
  .nav a.active { color: var(--gold); }

  .page {
    position: absolute; left: 183px; top: 84px; width: 933px; height: 728px;
    background: var(--panel); border-radius: 4px 4px 0 0;
  }
  .sidebar {
    position: absolute; left: 0; top: 0; width: 208px; height: 100%;
    border-right: 1px solid var(--divider);
  }
  .ad-box {
    position: absolute; left: 11px; top: 35px; width: 188px; height: 64px;
    background: #fff; border: 1px solid #999;
    display: flex; align-items: center; justify-content: center;
    font-size: 30px; font-weight: 700; color: #5a4a2a;
  }
  .view-switch {
    position: absolute; left: 16px; top: 136px; width: 166px; height: 33px;
    background: #eee; border-radius: 4px;
    font-size: 10px; color: #555; letter-spacing: 0.6px;
    display: flex; align-items: center; justify-content: flex-end; padding-right: 7px;
  }
  .view-switch a { color: var(--gold); margin: 0 4px; }
  .view-switch a:last-child { margin-right: 0; }
  .side-note { position: absolute; left: 16px; top: 202px; width: 170px; font-size: 13px; line-height: 20px; letter-spacing: 0.6px; }
  .side-note h3 { color: var(--gold); font-size: 13px; font-weight: 700; margin-bottom: 20px; }
  .side-note p { font-weight: 700; }

  .content { position: absolute; left: 224px; top: 0; width: 690px; }
  .content h1 {
    margin-top: 17px; font-size: 25px; font-weight: 400; color: var(--gold-light);
    letter-spacing: 0.8px; line-height: 34px;
  }
  .hero {
    margin-top: 15px; width: 622px; height: 411px;
    background: radial-gradient(ellipse at 45% 72%, #7a3a1c 0%, #5a2c14 22%, transparent 45%),
                linear-gradient(180deg, #3a3633 0%, #8c8782 35%, #e8e6e2 62%, #cfc9c3 100%);
  }
  .copy { margin-top: 17px; font-size: 13px; line-height: 20px; font-weight: 700; letter-spacing: 0.6px; }
  .copy p + p { margin-top: 20px; }
  .copy a { color: var(--gold); }

  .footer {
    position: absolute; left: 183px; top: 829px; width: 933px; height: 55px;
    border-radius: 5px 5px 0 0;
    background: linear-gradient(180deg, var(--bar-top), var(--bar-bottom));
    font-size: 11px; color: var(--muted); letter-spacing: 0.8px;
    display: flex; justify-content: space-between; align-items: center; padding: 0 18px;
  }
  .footer svg { vertical-align: -2px; }
</style>
</head>
<body>
  <div class="brand">
    <span class="brand-dot"></span>
    <span class="brand-name">FORNVALT</span>
  </div>

  <nav class="nav">
    <a class="active" href="#">Start</a>
    <a href="#">Kontakt</a>
    <a href="#">Unser Produkt</a>
    <a href="#">Preise</a>
    <a href="#">Partner</a>
    <a href="#">Ihr Weg zum Maßschuh</a>
  </nav>

  <main class="page">
    <aside class="sidebar">
      <div class="ad-box">Webova</div>
      <div class="view-switch">Ansicht: <a href="#">Galerie</a> | <a href="#">Liste</a></div>
      <div class="side-note">
        <h3>Platz für weitere Inhaltselement</h3>
        <p>Es erscheint unterhalb des Menüs der zweiten Ebene. Die Webova Werbebox darüber bitte wegdenken.</p>
      </div>
    </aside>

    <section class="content">
      <h1>Maßschuhe à la carte.</h1>
      <div class="hero" role="img" aria-label="Foto: braune Budapester Maßschuhe auf einer weiß gedeckten Tafel"></div>
      <div class="copy">
        <p>Was dürfen wir servieren?</p>
        <p>Von schlicht und elegant, klassisch bis sportlich, trendig oder bequem:<br>
        Wir können Ihnen jeden Wunsch erfüllen.<br>
        Sei es der Nachbau eines Lieblingsschuhs, der nicht mehr erhältlich ist,<br>
        seien es Probleme mit Konfektionsschuhen<br>
        oder ausgefallene Wünsche hinsichtlich Farbe, Form oder Material:</p>
        <p>Wir helfen Ihnen gerne weiter!</p>
        <p>Natürlich halten wir auch schon <a href="#">Menüvorschläge</a> bereit.</p>
      </div>
    </section>
  </main>

  <footer class="footer">
    <span>Impressum |
      <svg width="14" height="13" viewBox="0 0 14 13"><rect x="3" y="0" width="8" height="5" fill="#ddd"/><rect x="0" y="5" width="14" height="6" fill="#bbb"/><rect x="3" y="9" width="8" height="4" fill="#fff"/></svg>
      Druckversion | Sitemap</span>
    <span>Webova-Logout | Bearbeiten</span>
  </footer>
</body>
</html>
```